Investment Advisor E-Newsletter Banner Design

I need a banner designed for an email newsletter that will be sent monthly to clients and prospects. We want to see designs that are elegant and use our logo well. The banner should be 922x150px and should go well with the www.bhtlwest.com website. Should include Logo and email and phone number.

Target Market(s)

High net worth investors

Number of Pages Required

1 page

Requirements
Must have
• logo, place for email (info@bhtlwest.com) and phone number (555-219-0387), colors and design that work well with www.bhtlwest.com website

```html
<!DOCTYPE html>
<html lang="en">
<head>
<meta charset="utf-8">
<title>Bayhill Trust West – Newsletter Banners</title>
<link href="https://fonts.googleapis.com/css2?family=Noto+Serif:wght@400;700&display=swap" rel="stylesheet">
<style>
  :root {
    --stage: #121517;
    --navy: #2b2a7c;
    --lavender: #7a77bd;
    --ink: #2b2b2b;
    --frame: #ffffff;
    --arc-grey: #5f6062;
    --snow-top: #f7f8fb;
    --snow-low: #cfd4de;
  }
  * { box-sizing: border-box; margin: 0; padding: 0; }
  html, body { width: 1200px; height: 671px; overflow: hidden; }
  body {
    background: var(--stage);
    font-family: "Noto Serif", Georgia, serif;
    position: relative;
  }
  .banner {
    position: absolute;
    left: 162px;
    width: 877px;
    height: 147px;
    border: 2px solid var(--frame);
    border-radius: 3px;
    overflow: hidden;
    background: linear-gradient(180deg, var(--snow-top) 0%, #eef0f5 45%, var(--snow-low) 100%);
  }
  .banner--headline { top: 165px; }
  .banner--contact { top: 364px; }

  .banner__scene { position: absolute; inset: 0; width: 100%; height: 100%; }

  .brand {
    position: absolute;
    left: 36px;
    top: 46px;
    display: flex;
    align-items: center;
    gap: 12px;
  }
  .brand__dot {
    width: 42px; height: 42px;
    border-radius: 50%;
    background: var(--navy);
  }
  .brand__name {
    font-size: 27px;
    font-weight: 400;
    color: var(--navy);
    white-space: nowrap;
  }

  .headline {
    position: absolute;
    left: 336px;
    top: 12px;
    line-height: 1;
  }
  .headline__lead { font-size: 27px; color: var(--navy); font-weight: 400; }
  .headline__main { font-size: 41px; color: var(--ink); font-weight: 700; margin-top: 2px; }

  .pill {
    position: absolute;
    display: flex;
    align-items: center;
    border-radius: 14px;
    color: #fff;
    font-weight: 700;
    white-space: nowrap;
  }
  .pill--phone { background: var(--navy); }
  .pill--email { background: var(--lavender); }
  .pill__icon {
    flex: none;
    border-radius: 50%;
    border: 2px solid #fff;
    display: flex; align-items: center; justify-content: center;
  }
  .pill--phone .pill__icon { background: var(--lavender); }
  .pill--email .pill__icon { background: var(--navy); }
  .pill__text { flex: 1; text-align: center; }

  .pill--small { height: 26px; width: 203px; font-size: 16px; }
  .pill--small .pill__icon { width: 30px; height: 30px; margin-left: -2px; }
  .pill--large { height: 30px; width: 232px; font-size: 19px; border-radius: 15px; }
  .pill--large .pill__icon { width: 34px; height: 34px; margin-left: -2px; }
</style>
</head>
<body>

  <section class="banner banner--headline">
    <svg class="banner__scene" viewBox="0 0 877 147" preserveAspectRatio="none">
      <defs>
        <linearGradient id="deskPhoto" x1="0" y1="0" x2="1" y2="1">
          <stop offset="0" stop-color="#c9a57e"/>
          <stop offset="0.5" stop-color="#e7e3dc"/>
          <stop offset="1" stop-color="#8a6a55"/>
        </linearGradient>
      </defs>
      <path d="M604 0 Q620 110 700 147 L877 147 L877 0 Z" fill="var(--arc-grey)"/>
      <path d="M614 0 Q632 106 712 147 L877 147 L877 0 Z" fill="var(--lavender)"/>
      <path role="img" aria-label="Photo of advisors reviewing financial charts and a tablet on a desk" d="M620 0 Q640 102 722 147 L877 147 L877 0 Z" fill="url(#deskPhoto)"/>
    </svg>

    <div class="brand">
      <span class="brand__dot"></span>
      <span class="brand__name">Bayhill Trust West</span>
    </div>

    <div class="headline">
      <div class="headline__lead">Evidence-Based</div>
      <div class="headline__main">Investing</div>
    </div>

    <div class="pill pill--phone pill--small" style="left:226px; top:105px;">
      <span class="pill__icon">
        <svg width="16" height="16" viewBox="0 0 24 24"><path fill="#fff" d="M6.6 10.8a15.1 15.1 0 0 0 6.6 6.6l2.2-2.2c.3-.3.7-.4 1-.2 1.1.4 2.3.6 3.6.6.6 0 1 .4 1 1V20c0 .6-.4 1-1 1A17 17 0 0 1 3 4c0-.6.4-1 1-1h3.5c.6 0 1 .4 1 1 0 1.3.2 2.5.6 3.6.1.3 0 .7-.2 1z"/></svg>
      </span>
      <span class="pill__text">Call 555-219-0387</span>
    </div>

    <div class="pill pill--email pill--small" style="left:442px; top:105px;">
      <span class="pill__icon">
        <svg width="15" height="12" viewBox="0 0 24 18"><rect x="1" y="1" width="22" height="16" rx="2" fill="#fff"/><path d="M1 2l11 8 11-8" fill="none" stroke="var(--navy)" stroke-width="2"/></svg>
      </span>
      <span class="pill__text">info@bhtlwest.com</span>
    </div>
  </section>

  <section class="banner banner--contact">
    <svg class="banner__scene" viewBox="0 0 877 147" preserveAspectRatio="none">
      <defs>
        <linearGradient id="tabletPhoto" x1="0" y1="0" x2="1" y2="1">
          <stop offset="0" stop-color="#2f5f93"/>
          <stop offset="0.5" stop-color="#6f9cc8"/>
          <stop offset="1" stop-color="#1d3b63"/>
        </linearGradient>
      </defs>
      <path d="M604 0 Q620 110 700 147 L877 147 L877 0 Z" fill="var(--arc-grey)"/>
      <path d="M614 0 Q632 106 712 147 L877 147 L877 0 Z" fill="var(--lavender)"/>
      <path role="img" aria-label="Photo of a businessman holding a tablet with market charts" d="M620 0 Q640 102 722 147 L877 147 L877 0 Z" fill="url(#tabletPhoto)"/>
    </svg>

    <div class="brand">
      <span class="brand__dot"></span>
      <span class="brand__name">Bayhill Trust West</span>
    </div>

    <div class="pill pill--phone pill--large" style="left:338px; top:36px;">
      <span class="pill__icon">
        <svg width="18" height="18" viewBox="0 0 24 24"><path fill="#fff" d="M6.6 10.8a15.1 15.1 0 0 0 6.6 6.6l2.2-2.2c.3-.3.7-.4 1-.2 1.1.4 2.3.6 3.6.6.6 0 1 .4 1 1V20c0 .6-.4 1-1 1A17 17 0 0 1 3 4c0-.6.4-1 1-1h3.5c.6 0 1 .4 1 1 0 1.3.2 2.5.6 3.6.1.3 0 .7-.2 1z"/></svg>
      </span>
      <span class="pill__text">Call 555-219-0387</span>
    </div>

    <div class="pill pill--email pill--large" style="left:338px; top:80px;">
      <span class="pill__icon">
        <svg width="17" height="13" viewBox="0 0 24 18"><rect x="1" y="1" width="22" height="16" rx="2" fill="#fff"/><path d="M1 2l11 8 11-8" fill="none" stroke="var(--navy)" stroke-width="2"/></svg>
      </span>
      <span class="pill__text">info@bhtlwest.com</span>
    </div>
  </section>

</body>
</html>
```